Need 2 sided card for Loomfield Goods Co. Logo supplied.

I am looking for a business card for my online craft supply business.

I have a very simple design already which I am kind of happy with (see attached pdf) - but would like suggestions for something a little more creative. Design MUST be clean. Super clean! Think thin lines and not blocks of color...

Design must be clean and crisp. No other colors other than in palette (see link below)

I would also like to possible incorporate my tagline - maybe on the front but definitely on the back:
"HobbyNest Ideas & Making Materials"

Logo file is supplied, but I think spacing on the card may required the wording to be moved underneaths the camera icon - which is fine. Font in logo is Maven Pro. OPEN TO USE OF OTHER FONTS ON CARD BUT MUST BE CLEAN DESIGN.

FRONT OF CARD
All information on attached pdf is correct and should be shown in your design.

BACK OF CARD
Needs to show www.tinselbrookstore.com and maybe logo repeat and tagline.

SIZE
New Zealand sized - meaning finished card will be 90 x 55mm
Printing requirements: printed area is 90mm x 55mm with a 2mm bleed all round.

COLORS
Color palette used in logo can be seen here for HEX and RGB reference: http://www.huegatherly.net/palette/8802417/website

NOTE: PAYMENT WILL BE MADE FOR THE BEST DESIGN - EVEN IF I DECIDE NOT TO USE IT.
Updates

Thank you all so much for your designs. I will be providing feedback to ALL designers tomorrow. This weekend is a holiday weekend here in New Zealand and so no work for a few days. Thank-you again - I appreciate your time and creativity!

Industry/Entity Type

Camera

Font styles to use
Other font styles liked:
• Maven Pro - open to others

Requirements
Must have
• Clean design. Logo must be prominent for brand recognition. All contact information must be shown.
Nice to have
• Tagline - at least on reverse

```html
<!DOCTYPE html>
<html lang="en">
<head>
<meta charset="utf-8">
<title>Loomfield – Business Card</title>
<link href="https://fonts.googleapis.com/css2?family=Maven+Pro:wght@400&family=Open+Sans:wght@400;600&family=Cinzel:wght@700&display=swap" rel="stylesheet">
<style>
  :root {
    --bg: #e6e4e1;
    --card: #ffffff;
    --ink: #4d4b4b;
    --olive: #c2bd2a;
    --orange: #ee6133;
    --teal: #4fa594;
    --edge: #d9d7d4;
  }
  * { margin: 0; padding: 0; box-sizing: border-box; }
  html, body { width: 1200px; height: 1200px; overflow: hidden; }
  body {
    background: var(--bg);
    position: relative;
    font-family: "Open Sans", Arial, sans-serif;
    color: var(--ink);
  }
  .card {
    position: absolute;
    left: 180px;
    width: 840px;
    height: 513px;
    background: var(--card);
    box-shadow: 0 6px 18px rgba(0,0,0,0.12);
    border: 1px solid var(--edge);
  }
  .card--back { top: 58px; }
  .card--front { top: 629px; }

  .wordmark {
    display: flex;
    align-items: center;
    gap: 22px;
    font-family: "Maven Pro", Arial, sans-serif;
    font-weight: 400;
    color: var(--ink);
    line-height: 1;
  }
  .wordmark__dot {
    border-radius: 50%;
    background: var(--orange);
    flex: none;
  }

  /* back */
  .card--back .wordmark {
    position: absolute;
    top: 150px;
    left: 0; right: 0;
    justify-content: center;
    font-size: 96px;
  }
  .card--back .wordmark__dot { width: 60px; height: 60px; }
  .back-url {
    position: absolute;
    top: 360px;
    left: 0; right: 0;
    text-align: center;
    font-size: 30px;
    letter-spacing: 0.5px;
  }

  /* front */
  .card--front .wordmark {
    position: absolute;
    top: 110px;
    right: 70px;
    font-size: 68px;
  }
  .card--front .wordmark__dot { width: 42px; height: 42px; }
  .holder-name {
    position: absolute;
    left: 56px;
    top: 278px;
    font-family: "Cinzel", Georgia, serif;
    font-weight: 700;
    font-size: 28px;
    letter-spacing: 1px;
  }
  .contacts {
    position: absolute;
    top: 340px;
    list-style: none;
    font-size: 21px;
  }
  .contacts--left { left: 56px; }
  .contacts--right { left: 420px; top: 322px; }
  .contacts li {
    display: flex;
    align-items: center;
    gap: 12px;
    height: 42px;
    white-space: nowrap;
  }
  .icon {
    width: 30px; height: 30px;
    flex: none;
    display: block;
  }
</style>
</head>
<body>

  <section class="card card--back" aria-label="Card back">
    <div class="wordmark"><span class="wordmark__dot"></span>Loomfield</div>
    <p class="back-url">www.tinselbrookstore.com</p>
  </section>

  <section class="card card--front" aria-label="Card front">
    <div class="wordmark"><span class="wordmark__dot"></span>Loomfield</div>
    <h1 class="holder-name">TESSA HARROWBY</h1>

    <ul class="contacts contacts--left">
      <li>
        <svg class="icon" viewBox="0 0 30 30"><rect width="30" height="30" fill="var(--orange)"/><path d="M8 12c0-3 3-4 7-4s7 1 7 4l-3 1-1-2h-6l-1 2zM10 14h10l1 8H9z" fill="#fff"/></svg>
        +64 (0) 3 555 0147
      </li>
      <li>
        <svg class="icon" viewBox="0 0 30 30"><rect width="30" height="30" fill="var(--olive)"/><rect x="10" y="6" width="10" height="18" rx="1.5" fill="none" stroke="#fff" stroke-width="2"/><rect x="12" y="9" width="6" height="6" fill="#fff"/></svg>
        +64 (0) 21 555 01938
      </li>
      <li>
        <svg class="icon" viewBox="0 0 30 30"><rect width="30" height="30" fill="var(--teal)"/><path d="M6 8h3l3 10h10l2-7H11" fill="none" stroke="#fff" stroke-width="2"/><circle cx="13" cy="22" r="1.6" fill="#fff"/><circle cx="21" cy="22" r="1.6" fill="#fff"/></svg>
        www.tinselbrookstore.com
      </li>
    </ul>

    <ul class="contacts contacts--right">
      <li>
        <svg class="icon" viewBox="0 0 30 30"><rect width="30" height="30" fill="var(--ink)"/><rect x="6" y="9" width="18" height="12" fill="none" stroke="#fff" stroke-width="2"/><path d="M6 9l9 7 9-7" fill="none" stroke="#fff" stroke-width="2"/></svg>
        tessa.harrowby@loomfieldnz.com
      </li>
      <li>
        <svg class="icon" viewBox="0 0 30 30"><rect width="30" height="30" fill="var(--teal)"/><circle cx="15" cy="15" r="8" fill="#fff"/></svg>
        Fanpage.net/loomfield
      </li>
      <li>
        <svg class="icon" viewBox="0 0 30 30"><rect width="30" height="30" fill="var(--orange)"/><circle cx="15" cy="15" r="8" fill="none" stroke="#fff" stroke-width="1.8"/><ellipse cx="15" cy="15" rx="3.5" ry="8" fill="none" stroke="#fff" stroke-width="1.5"/><path d="M7 15h16" stroke="#fff" stroke-width="1.5"/></svg>
        www.loomfieldnz.com
      </li>
    </ul>
  </section>

</body>
</html>
```